Sunny Trails and joy Business card

I have a logo, but will like a business card design. Is for a travel agency in Mexico. We focus in family experiences.

I will liek some thing different and unique, from the traditional business card, something to get remmeber for.

Business card information:

Leandro R. Quiroga
leandro@sunnytrailsjoy.example

Alameda 742, 3 piso
Col. Tepalcatl
Mexico, D.F. 04910

office: (55) 4821-7390
mobile: (55) 7034-1258

www.sunnytrailsjoy.example
@sunnytjoy
blog: sunnytrailsandjoy.blog.example
facebook: SunnyTrailsAndJoy

```html
<!DOCTYPE html>
<html lang="es">
<head>
<meta charset="utf-8">
<title>Sunny Trails and joy — Business card</title>
<link rel="stylesheet" href="https://fonts.googleapis.com/css2?family=Varela+Round&display=swap">
<style>
  :root {
    --brand-blue: #2a5bb0;
    --brand-blue-deep: #1d4690;
    --brand-blue-light: #3c6fc4;
    --paper: #ffffff;
    --ink-grey: #8c949e;
    --ink-soft: #aab1ba;
    --dot: #c7b98a;
    --stage: #e9ebee;
  }
  * { box-sizing: border-box; margin: 0; padding: 0; }
  html, body { width: 1200px; height: 800px; overflow: hidden; }
  body {
    background: var(--stage);
    font-family: "Varela Round", "Arial Rounded MT Bold", sans-serif;
    display: flex;
    align-items: center;
    justify-content: center;
    gap: 40px;
  }
  .card {
    width: 540px;
    height: 309px;
    position: relative;
    box-shadow: 0 6px 18px rgba(0,0,0,.18);
    overflow: hidden;
  }

  /* Brand mark */
  .brand {
    display: flex;
    align-items: center;
    justify-content: center;
    gap: 10px;
    color: var(--brand-blue);
    font-size: 24px;
    letter-spacing: .5px;
  }
  .brand-dot {
    width: 22px; height: 22px;
    border-radius: 50%;
    background: var(--brand-blue);
  }

  /* Front */
  .card-front { background: var(--paper); }
  .card-front .brand { position: absolute; top: 52px; left: 0; right: 0; }
  .info {
    position: absolute;
    left: 20px; right: 20px;
    top: 125px;
    height: 112px;
    border-top: 2px dotted var(--dot);
    border-bottom: 2px dotted var(--dot);
    display: grid;
    grid-template-columns: 1fr 200px;
  }
  .contact {
    padding: 12px 10px 0 4px;
    border-right: 2px dotted var(--dot);
    color: var(--brand-blue);
  }
  .phones { font-size: 12px; white-space: nowrap; }
  .phones .label { color: var(--ink-soft); }
  .address { font-size: 9.5px; margin-top: 5px; white-space: nowrap; }
  .social {
    margin-top: 10px;
    display: grid;
    grid-template-columns: 1fr 1fr;
    gap: 4px 8px;
    font-size: 7.5px;
    color: var(--ink-grey);
  }
  .social span { display: flex; align-items: center; gap: 4px; white-space: nowrap; }
  .social-square {
    width: 8px; height: 8px;
    background: var(--brand-blue-light);
    flex: none;
  }
  .person {
    display: flex;
    flex-direction: column;
    justify-content: center;
    padding-left: 14px;
  }
  .person-name { color: var(--brand-blue); font-size: 18px; white-space: nowrap; }
  .person-email { color: var(--brand-blue); font-size: 8.5px; margin-top: 18px; }

  /* Back */
  .card-back {
    background:
      radial-gradient(circle at 30% 20%, rgba(255,255,255,.08), transparent 60%),
      linear-gradient(160deg, var(--brand-blue-light), var(--brand-blue) 50%, var(--brand-blue-deep));
  }
  .band {
    position: absolute;
    left: 0; right: 0;
    top: 98px; height: 112px;
    background: var(--paper);
    display: flex;
    align-items: center;
    justify-content: center;
  }
  .band::before, .band::after {
    content: "";
    position: absolute;
    left: 0; right: 0;
    height: 6px;
    background:
      linear-gradient(135deg, var(--paper) 50%, transparent 50%) 0 0 / 6px 6px repeat-x,
      linear-gradient(225deg, var(--paper) 50%, transparent 50%) 0 0 / 6px 6px repeat-x;
  }
  .band::before { top: -6px; transform: scaleY(-1); }
  .band::after { bottom: -6px; }
</style>
</head>
<body>
  <section class="card card-front" aria-label="Front of business card">
    <div class="brand"><span class="brand-dot"></span>Sunny Trails and joy</div>
    <div class="info">
      <div class="contact">
        <p class="phones"><span class="label">office:</span> (55) 4821-7390 <span class="label">mobile:</span> (55) 7034-1258</p>
        <p class="address">Alameda 742, 3 piso Col. Tepalcatl, Mexico, D.F. 04910</p>
        <div class="social">
          <span>www.sunnytrailsjoy.example</span>
          <span><i class="social-square"></i>SunnyTrailsAndJoy</span>
          <span>@sunnytjoy</span>
          <span><i class="social-square"></i>sunnytrailsandjoy.blog.example</span>
        </div>
      </div>
      <div class="person">
        <p class="person-name">Leandro R. Quiroga</p>
        <p class="person-email">leandro@sunnytrailsjoy.example</p>
      </div>
    </div>
  </section>

  <section class="card card-back" aria-label="Back of business card">
    <div class="band">
      <div class="brand"><span class="brand-dot"></span>Sunny Trails and joy</div>
    </div>
  </section>
</body>
</html>
```